mobile app design: app provides timely Natural gas pipeline information (similar to weather, etc)

we are going to create and publish an app in all the three markets.( android, ios,windows). we have wire framed mostly all the screens. the designers are to provide the layout, design & background. The following are the most important things.

1. the app's target audience are guys working in the natural gas industry in the US.
2. the app provides the customer with latest pipeline information
3. the trial version is free and will provide information about one pipeline
4. slides 1 to 5 are trial version slides.
5. slides 6 onwards the customer chooses.
6. the final product is displayed in a grid.
7. the app will be developed using html5 and css3.
8. customer will pay per pipeline for the information. ( in app payment)
9 there are similiar ( complementary) products which provide weekly storage data at vexlo mart and quorbit app store.
10. i have attached the pdf document of the wireframe.
11.i have attached the logo
12. no name has been thought out yet.

Hi guys

I have a main question for the designer community .

1. is it possible to combine some of the pages ( screens  ) into one or two. use your gut feel. if not it is ok.

2. check out the flow, the color, the background , the font and the font size. it should be pleasing.

thanx

Tomek

Natural Gas

```html
<!DOCTYPE html>
<html lang="en">
<head>
<meta charset="utf-8">
<title>Pipeline Region Select</title>
<link rel="stylesheet" href="https://fonts.googleapis.com/css2?family=Arimo:wght@400;600&display=swap">
<style>
  :root {
    --bg: #ffffff;
    --ink: #111111;
    --label: #5c5c5c;
    --brand: #1b55a3;
    --brand-dark: #0f4a92;
    --divider: #ececec;
    --photo-light: #e6e9ed;
    --photo-mid: #cfd6de;
    --photo-sky: #dfe7ef;
    --photo-warm: #e9e3cf;
  }
  * { margin: 0; padding: 0; box-sizing: border-box; }
  html, body { width: 1200px; height: 2226px; overflow: hidden; background: var(--bg); }
  body { font-family: "Arimo", Helvetica, Arial, sans-serif; position: relative; }

  .hero-photo {
    position: absolute; left: 0; top: 0; width: 1200px; height: 435px;
    background: linear-gradient(90deg, var(--photo-sky) 0%, var(--photo-light) 25%, var(--photo-mid) 45%, var(--photo-light) 60%, var(--photo-mid) 80%, var(--photo-sky) 100%);
  }
  .hero-photo::after {
    content: ""; position: absolute; left: 0; right: 0; bottom: 0; height: 90px;
    background: linear-gradient(180deg, rgba(233,227,207,0) 0%, var(--photo-warm) 100%);
    opacity: .6;
  }

  .status-bar {
    position: absolute; left: 0; top: 0; width: 1200px; height: 60px;
    display: flex; align-items: center; justify-content: space-between;
    padding: 0 28px; color: var(--ink); font-size: 42px; font-weight: 600;
  }
  .status-left, .status-right { display: flex; align-items: center; gap: 12px; }
  .status-time { position: absolute; left: 0; right: 0; text-align: center; pointer-events: none; }

  .region-list { position: absolute; left: 0; top: 435px; width: 1200px; list-style: none; background: var(--bg); }
  .region-item {
    height: 176px; display: flex; align-items: center; padding-left: 63px;
    border-bottom: 3px solid var(--divider);
  }
  .region-item:last-child { border-bottom: none; }
  .checkbox {
    width: 90px; height: 90px; border: 5px solid var(--brand); border-radius: 4px;
    display: flex; align-items: center; justify-content: center; flex: none;
  }
  .region-name { margin-left: 50px; font-size: 56px; color: var(--label); }

  .footer-photo {
    position: absolute; left: 0; top: 1491px; width: 1200px; height: 735px;
    background: linear-gradient(90deg, var(--photo-light) 0%, var(--photo-mid) 18%, var(--photo-warm) 40%, var(--photo-light) 55%, var(--photo-mid) 75%, var(--photo-light) 100%);
  }
  .next-button {
    position: absolute; left: 516px; top: 1668px; width: 110px; height: 110px;
    background: var(--brand-dark); border-radius: 12px;
    display: flex; align-items: center; justify-content: center;
  }
</style>
</head>
<body>
  <div class="hero-photo" role="img" aria-label="Pale photo of natural gas plant stacks and pipes"></div>

  <header class="status-bar">
    <div class="status-left">
      <svg width="110" height="24" viewBox="0 0 110 24" aria-hidden="true">
        <circle cx="11" cy="12" r="9" fill="#111"/><circle cx="33" cy="12" r="9" fill="#111"/><circle cx="55" cy="12" r="9" fill="#111"/>
        <circle cx="77" cy="12" r="8" fill="none" stroke="#111" stroke-width="2"/><circle cx="99" cy="12" r="8" fill="none" stroke="#111" stroke-width="2"/>
      </svg>
      <span class="carrier">KLOVA</span>
      <svg width="44" height="34" viewBox="0 0 44 34" aria-hidden="true">
        <path d="M22 32 L14 23 A12 12 0 0 1 30 23 Z" fill="#111"/>
        <path d="M6 15 A23 23 0 0 1 38 15" fill="none" stroke="#111" stroke-width="5"/>
        <path d="M1 8 A31 31 0 0 1 43 8" fill="none" stroke="#111" stroke-width="5"/>
      </svg>
    </div>
    <div class="status-time">4:21 PM</div>
    <div class="status-right">
      <svg width="22" height="38" viewBox="0 0 22 38" aria-hidden="true">
        <path d="M3 10 L18 26 L10 34 L10 4 L18 12 L3 28" fill="none" stroke="#555" stroke-width="3"/>
      </svg>
      <span>100%</span>
      <svg width="96" height="38" viewBox="0 0 96 38" aria-hidden="true">
        <rect x="2" y="4" width="84" height="30" rx="5" fill="none" stroke="#111" stroke-width="3"/>
        <rect x="7" y="9" width="74" height="20" rx="2" fill="#111"/>
        <rect x="88" y="13" width="6" height="12" rx="2" fill="#111"/>
      </svg>
    </div>
  </header>

  <ul class="region-list">
    <li class="region-item">
      <span class="checkbox is-checked">
        <svg width="56" height="44" viewBox="0 0 56 44" aria-hidden="true"><path d="M5 23 L20 37 L51 6" fill="none" stroke="var(--brand)" stroke-width="8"/></svg>
      </span>
      <span class="region-name">NorthEast</span>
    </li>
    <li class="region-item"><span class="checkbox"></span><span class="region-name">MidWest</span></li>
    <li class="region-item"><span class="checkbox"></span><span class="region-name">SouthEast</span></li>
    <li class="region-item"><span class="checkbox"></span><span class="region-name">SouthWest</span></li>
    <li class="region-item"><span class="checkbox"></span><span class="region-name">Central</span></li>
    <li class="region-item"><span class="checkbox"></span><span class="region-name">West</span></li>
  </ul>

  <div class="footer-photo" role="img" aria-label="Pale photo of gas pipeline machinery with yellow pipes"></div>

  <div class="next-button" aria-label="Next">
    <svg width="40" height="52" viewBox="0 0 40 52" aria-hidden="true"><path d="M10 8 L28 26 L10 44" fill="none" stroke="#fff" stroke-width="8"/></svg>
  </div>
</body>
</html>
```